Accounting business needs business card

I have a business card but need something better. I want the colour changed and the design to be better. I have uploaded a picture of my new sign that is grey in colour, i would like to incorporate these colours.

```html
<!DOCTYPE html>
<html lang="en">
<head>
<meta charset="utf-8">
<title>Lumen Tax — Business Card</title>
<link href="https://fonts.googleapis.com/css2?family=Montserrat:wght@500;600&family=Roboto:wght@300;400&display=swap" rel="stylesheet">
<style>
  :root {
    --backdrop: #d3d3ce;
    --card-white: #ffffff;
    --charcoal: #3a3a3a;
    --ink: #2b2b2b;
    --teal: #1fae8c;
    --sky: #1ab4e8;
    --royal: #0d5aa7;
    --gold: #f7cf1d;
    --seal-green: #b6c832;
  }
  * { box-sizing: border-box; margin: 0; padding: 0; }
  html, body { width: 1200px; height: 1058px; overflow: hidden; }
  body {
    background: var(--backdrop);
    font-family: "Roboto", Arial, sans-serif;
    position: relative;
  }
  .card {
    position: absolute;
    left: 240px;
    width: 720px;
    height: 411px;
    box-shadow: 0 10px 24px rgba(0,0,0,0.18);
  }
  .card--front { top: 88px; background: var(--card-white); }
  .card--back { top: 559px; background: var(--charcoal); overflow: hidden; }

  .identity { position: absolute; left: 48px; top: 52px; width: 330px; }
  .identity__name {
    font-family: "Montserrat", Arial, sans-serif;
    font-weight: 600;
    font-size: 28px;
    line-height: 36px;
    letter-spacing: 2.5px;
    color: var(--teal);
    white-space: nowrap;
  }
  .identity__line {
    font-weight: 300;
    font-size: 17px;
    line-height: 24px;
    color: var(--ink);
    letter-spacing: 0.4px;
  }

  .accreditations {
    position: absolute; left: 48px; top: 168px;
    display: flex; align-items: center; gap: 18px;
  }
  .accreditations svg { display: block; }

  .contact { position: absolute; left: 48px; top: 276px; list-style: none; }
  .contact li {
    display: flex; align-items: center; gap: 12px;
    font-weight: 300; font-size: 20px; color: var(--ink);
    letter-spacing: 0.5px; line-height: 31px;
  }
  .contact svg { width: 14px; height: 14px; flex: none; }

  .brand-mark {
    position: absolute; left: 400px; top: 40px;
    width: 290px; height: 250px;
    display: flex; align-items: center; justify-content: center; gap: 16px;
  }
  .brand-mark__dot {
    width: 58px; height: 58px; border-radius: 50%;
    border: 6px solid var(--ink); flex: none;
  }
  .brand-mark__name {
    font-weight: 400; font-size: 32px; letter-spacing: 2px; color: var(--ink);
    white-space: nowrap;
  }

  .back-pattern { position: absolute; inset: 0; background: radial-gradient(circle at 60% 40%, #414141, #363636); }
  .back-mark {
    position: absolute; right: 110px; top: 176px;
    display: flex; align-items: center; gap: 10px;
  }
  .back-mark__dot { width: 18px; height: 18px; border-radius: 50%; border: 2px solid #fff; }
  .back-mark__name { font-weight: 400; font-size: 22px; letter-spacing: 1.5px; color: #fff; }
</style>
</head>
<body>

<section class="card card--front" aria-label="Business card front">
  <div class="identity">
    <h1 class="identity__name">DANA WHITFORD</h1>
    <p class="identity__line">CPA, MTAX, BCOM (Acc &amp; Fin)</p>
    <p class="identity__line">Taxation &amp; Business Accountant</p>
  </div>

  <div class="accreditations">
    <svg width="50" height="50" viewBox="0 0 62 62" aria-label="Registration seal">
      <circle cx="31" cy="31" r="29" fill="#fff" stroke="#999" stroke-width="1.5"/>
      <circle cx="31" cy="31" r="17" fill="var(--seal-green)"/>
    </svg>
    <svg width="66" height="66" viewBox="0 0 82 82" aria-label="Software partner badge">
      <circle cx="41" cy="41" r="40" fill="var(--sky)"/>
    </svg>
    <svg width="150" height="66" viewBox="0 0 190 84" preserveAspectRatio="none" aria-label="Professional body badge">
      <rect x="0" y="0" width="130" height="84" fill="var(--royal)"/>
      <rect x="130" y="0" width="60" height="84" fill="var(--gold)"/>
    </svg>
  </div>

  <ul class="contact">
    <li>
      <svg viewBox="0 0 14 14"><path d="M3 1 L5 1 L6 4 L4.5 5 Q5.5 8 9 9.5 L10 8 L13 9 L13 11 Q12 13 10 13 Q2 11 1 3 Q1 1 3 1Z" fill="var(--teal)"/></svg>
      0412 555 018
    </li>
    <li>
      <svg viewBox="0 0 14 14"><rect x="1" y="3" width="12" height="8.5" fill="none" stroke="var(--teal)" stroke-width="1.4"/><path d="M1 3 L7 8 L13 3" fill="none" stroke="var(--teal)" stroke-width="1.4"/></svg>
      dana@lumentax.com.au
    </li>
    <li>
      <svg viewBox="0 0 14 14"><circle cx="7" cy="7" r="6" fill="none" stroke="var(--teal)" stroke-width="1.3"/><path d="M1 7 H13 M7 1 Q3.5 7 7 13 M7 1 Q10.5 7 7 13" fill="none" stroke="var(--teal)" stroke-width="1.1"/></svg>
      www.lumentax.com.au
    </li>
  </ul>

  <div class="brand-mark">
    <span class="brand-mark__dot"></span>
    <span class="brand-mark__name">LUMEN TAX</span>
  </div>
</section>

<section class="card card--back" aria-label="Business card back">
  <div class="back-pattern" role="img" aria-label="Tone-on-tone embossed repeating monogram pattern on charcoal stock"></div>
  <div class="back-mark">
    <span class="back-mark__dot"></span>
    <span class="back-mark__name">LUMEN TAX</span>
  </div>
</section>

</body>
</html>
```